Tarvolin - Clever Border Flow Lifting Traders

Web Design for international start-up, which is automating customs clearance processes for forwarding companies by applying a web application, which is operating with artificial intelligence and robotic process automation. Tarvolin pursues the vision of supporting forwarding companies successfully in becoming digital masters and co-creates innovative software solutions with all participants (ex- and importers of goods) along value-added chains. With intelligent/smart/digital customs clearance software or in other words, a virtual customs clearance roboter tailord to the customers needs, we are transforming businesses. The website could look like this:

https://www.krt-example.com/uk-en/index.php
or
https://sitepress-example.com/theme/marlowfield

Please use colours and designs you think would be the best fit. These websites are just here to give you an idea of how the webdesign could look like. Use the attached logo design as a basis for further web design. You can use the provided pictures, but you can also use your own ones, if you think they are better suited. But please take care, that they have a high resolution quality.

Description of Website: The website is transparent and modern. It provides seven pages such as homepage, products, web app, the about us, working at Tarvolin, News, contact us and search results page. The homepage or landing page should be filled with a short description of the company, what Tarvolin is doing, how they will support its customers and will also include a video of the provided solution. Products provide obviously information about different products and their characteristics. Web app page includes information about principles and technologies that get the software going. The about us page includes unique advantages and value propositions for customers and the contact us, as the name already says, will provide contact information and possibilities to contact us. The rest is also obvious (for additional information look up the website of KRT, priorly provided link - the page is also available in english).

If you have any questions, I am happy to answer them any time.
Updates

I have to think about the text that I want to have included into the design and hadn't have the time to compose it.

Target Market(s)

Forwarding Companies, Ex-/Importers

Industry/Entity Type

It Company

Number of Pages Required

5+ page

Requirements
Must have
• The web design should be designes according to the attached logo of Tarvolin.

```html
<!DOCTYPE html>
<html lang="en">
<head>
<meta charset="utf-8">
<title>Tarvolin – Clever Border Flow Lifting Traders</title>
<link href="https://fonts.googleapis.com/css2?family=Montserrat:wght@400;500;600&display=swap" rel="stylesheet">
<style>
:root{
  --backdrop:#ececec;
  --navy:#1b3d78;
  --navy-deep:#14305f;
  --cyan:#1fb6e0;
  --ink:#2a2f3a;
  --muted:#6b7280;
  --white:#ffffff;
  --line:#d9dde4;
}
*{box-sizing:border-box;margin:0;padding:0}
html,body{width:1200px;height:1200px;overflow:hidden;background:var(--backdrop);font-family:'Montserrat',sans-serif;color:var(--ink)}
.stage{position:absolute;left:0;top:0;width:1500px;height:1500px;transform:scale(.8);transform-origin:0 0}
.page{position:absolute;left:571px;top:38px;width:330px;height:1426px;background:var(--white);overflow:hidden}
.abs{position:absolute}
.tiny{font-size:3.2px;line-height:5.2px;color:var(--muted)}
.topbar{left:0;top:0;width:330px;height:15px;background:var(--navy);color:var(--white);font-size:3.6px;display:flex;align-items:center;justify-content:space-between;padding:0 10px}
.topbar span{margin-left:8px}
.brand{font-weight:500;color:var(--navy);font-size:12px;letter-spacing:.2px}
.brand-tag{font-size:2.6px;color:var(--muted)}
.nav{left:123px;top:25px;display:flex;gap:9px;font-size:3.6px;color:var(--ink)}
.nav .on{color:var(--cyan)}
.quote{left:293px;top:24px;width:27px;height:6px;background:var(--cyan);color:var(--white);font-size:2.8px;text-align:center;line-height:6px}
.ph{background:linear-gradient(135deg,#c9d2dc,#8f9cac)}
.hero{left:0;top:42px;width:330px;height:138px;background:linear-gradient(90deg,#eef1f5 0%,#dde3ea 45%,#5f6f82 75%,#3b4656 100%)}
.hero-title{left:18px;top:82px;color:var(--navy);font-size:8px;letter-spacing:.8px;line-height:11px}
.hero-rule{left:14px;top:82px;width:1px;height:32px;background:var(--navy)}
h2{font-weight:500;color:var(--ink)}
.btn{background:var(--cyan);color:var(--white);font-size:4px;text-align:center}
.feat{width:90px;height:22px;background:var(--navy);color:var(--white);font-size:4.8px;line-height:6px;display:flex;align-items:center;gap:5px;padding-left:5px}
.dark{background:linear-gradient(180deg,#10234a,#1b3d78)}
.card{background:var(--white);text-align:center;padding:8px 7px}
.card h3{font-weight:400;font-size:5.4px;margin:6px 0 6px}
.card p{font-size:3.2px;line-height:5.3px;color:var(--muted)}
.pcard{background:var(--navy);color:var(--white);text-align:center;padding:8px 7px}
.pcard h3{font-weight:500;font-size:6px;margin-bottom:8px}
.pcard p{font-size:3.2px;line-height:5.3px;opacity:.9}
.pcard .more{width:26px;height:6px;border:.6px solid #fff;border-radius:3px;margin:6px auto 0;font-size:2.4px;line-height:5px}
.field{background:var(--white);height:8px;font-size:2.6px;color:var(--muted);padding:1.5px 3px}
.news{background:var(--white);box-shadow:0 1px 3px rgba(0,0,0,.18)}
.news h4{font-weight:500;font-size:3.6px;line-height:5px;color:var(--navy);margin:8px 6px 3px}
.news p{font-size:3.2px;line-height:5.3px;color:var(--muted);margin:0 6px}
.news .meta{font-size:2.6px;color:var(--navy);margin:6px 6px 0}
.foot{left:0;top:1308px;width:330px;height:118px;background:var(--navy);color:var(--white)}
.foot h5{font-weight:400;font-size:6.4px}
.foot li{list-style:none;font-size:3.6px;line-height:7.5px}
</style>
</head>
<body>
<div class="stage">
<main class="page">

  <div class="abs topbar">
    <div>✉ info@tarvolin-example.com &nbsp;☏ 000.0000.0000</div>
    <div><span>English</span><span>Log in</span><span>Sing Up</span></div>
  </div>

  <header>
    <div class="abs" style="left:12px;top:18px">
      <div class="brand">Tarvolin</div>
      <div class="brand-tag" style="margin-left:18px">Clever Border Flow</div>
    </div>
    <nav class="abs nav"><span class="on">HOME</span><span>ABOUT US</span><span>PRODUCT</span><span>SERVICE</span><span>NEWS</span><span>CONTACT US</span></nav>
    <div class="abs quote">Get a quote</div>
  </header>

  <section>
    <div class="abs hero" role="img" aria-label="Photo of a man with a headset working at a computer in a bright office"></div>
    <div class="abs hero-rule"></div>
    <div class="abs hero-title"><span style="font-size:6px">WE ARE</span><br>CO-CREATES INNOVATIVE<br>SOFTWARE SOLUTIONS</div>
    <p class="abs tiny" style="left:16px;top:118px;width:128px">Lorem ipsum dolor sit amet, consectetur adipiscing elit. Proin eget ornare lacus, in ullamcorper dolor. Nulla rhoncus pellentesque hendrerit. Nullam mollis mauris sed gravida posuere. Praesent eu risus tortor.</p>
  </section>

  <section>
    <div class="abs ph" style="left:18px;top:200px;width:122px;height:82px;background:linear-gradient(135deg,#d8c9a6,#7d8a9c)" role="img" aria-label="Photo of a team meeting around a whiteboard with sticky notes"></div>
    <h2 class="abs" style="left:155px;top:204px;font-size:6.6px">Who We Are ?</h2>
    <div class="abs" style="left:155px;top:216px;width:24px;height:.8px;background:var(--cyan)"></div>
    <p class="abs tiny" style="left:155px;top:223px;width:156px;text-align:justify">Lorem ipsum dolor sit amet, consectetur adipiscing elit. Proin eget ornare lacus, in ullamcorper dolor. Nulla rhoncus pellentesque hendrerit. Nullam mollis mauris sed gravida posuere. Praesent eu risus tortor. Donec pretium commodo mauris quis sodales. Vivamus feugiat blandit consequat. Integer suscipit ultrices dolor at malesuada. Suspendisse in est sed lacus pretium elementum.</p>
    <div class="abs btn" style="left:155px;top:272px;width:42px;height:10px;line-height:10px">Read More</div>

    <div class="abs feat" style="left:18px;top:300px">
      <svg width="12" height="12" viewBox="0 0 12 12"><circle cx="4" cy="4" r="2.5" fill="none" stroke="#fff" stroke-width="1"/><circle cx="8.5" cy="8.5" r="2" fill="none" stroke="#fff" stroke-width="1"/></svg>
      <span>Intelligent, Smart Digital<br>customs clearance</span></div>
    <div class="abs feat" style="left:121px;top:300px">
      <svg width="12" height="12" viewBox="0 0 12 12"><circle cx="6" cy="6" r="4.5" fill="none" stroke="#fff" stroke-width="1"/><circle cx="6" cy="6" r="1.6" fill="#fff"/></svg>
      <span>Robotic Process<br>Automation</span></div>
    <div class="abs feat" style="left:224px;top:300px">
      <svg width="14" height="12" viewBox="0 0 14 12"><rect x="1" y="2" width="12" height="7" fill="none" stroke="#fff" stroke-width="1"/><path d="M4 11h6" stroke="#fff"/></svg>
      <span>Innovative Software<br>Solutions</span></div>
  </section>

  <section class="abs dark" style="left:0;top:336px;width:330px;height:161px">
    <h2 class="abs" style="left:0;width:330px;top:16px;text-align:center;color:#fff;font-size:6.6px;font-weight:400">Why choose Us</h2>
    <p class="abs tiny" style="left:0;width:330px;top:25px;text-align:center;color:#c9d3e6;font-size:2.6px">Lorem ipsum dolor sit amet, consectetur adipiscing elit</p>
    <div class="abs" style="left:150px;top:34px;width:30px;height:.8px;background:#fff;opacity:.7"></div>
    <div class="abs card" style="left:22px;top:45px;width:85px;height:94px">
      <svg width="6" height="6" viewBox="0 0 6 6"><circle cx="3" cy="3" r="2.4" fill="none" stroke="#555" stroke-width=".6"/><path d="M3 1.5V3l1 .8" stroke="#555" stroke-width=".6" fill="none"/></svg>
      <h3>On time Service</h3>
      <p>Lorem ipsum dolor sit amet, consectetur adipiscing elit. Proin eget ornare lacus, in ullamcorper dolor. Nulla rhoncus pellentesque hendrerit. Nullam mollis mauris sed gravida posuere. Praesent eu risus tortor.</p>
    </div>
    <div class="abs card" style="left:119px;top:45px;width:85px;height:94px">
      <svg width="6" height="6" viewBox="0 0 6 6"><path d="M1 4V3a2 2 0 0 1 4 0v1" stroke="#555" stroke-width=".6" fill="none"/><rect x=".7" y="3.5" width="1" height="1.6" fill="#555"/><rect x="4.3" y="3.5" width="1" height="1.6" fill="#555"/></svg>
      <h3>Awesome Support</h3>
      <p>Lorem ipsum dolor sit amet, consectetur adipiscing elit. Proin eget ornare lacus, in ullamcorper dolor. Nulla rhoncus pellentesque hendrerit. Nullam mollis mauris sed gravida posuere. Praesent eu risus tortor.</p>
    </div>
    <div class="abs card" style="left:215px;top:45px;width:85px;height:94px">
      <svg width="6" height="6" viewBox="0 0 6 6"><circle cx="3" cy="1.8" r="1.3" fill="#333"/><path d="M.8 6a2.2 2.2 0 0 1 4.4 0z" fill="#333"/></svg>
      <h3>Expert Advisors</h3>
      <p>Lorem ipsum dolor sit amet, consectetur adipiscing elit. Proin eget ornare lacus, in ullamcorper dolor. Nulla rhoncus pellentesque hendrerit. Nullam mollis mauris sed gravida posuere. Praesent eu risus tortor.</p>
    </div>
  </section>

  <section>
    <h2 class="abs" style="left:24px;top:511px;font-size:6.4px">Our Mission &amp; Vission</h2>
    <div class="abs" style="left:24px;top:522px;width:24px;height:.8px;background:var(--cyan)"></div>
    <p class="abs tiny" style="left:24px;top:529px;width:160px">Lorem ipsum dolor sit amet, consectetur adipiscing elit. Proin eget ornare lacus, in ullamcorper dolor. Nulla rhoncus pellentesque hendrerit. Nullam mollis mauris sed gravida posuere.</p>
    <ul class="abs tiny" style="left:26px;top:550px;list-style:none">
      <li><span style="color:var(--cyan)">✓</span> Lorem ipsum dolor sit amet</li>
      <li><span style="color:var(--cyan)">✓</span> Lorem ipsum dolor sit amet</li>
      <li><span style="color:var(--cyan)">✓</span> Lorem ipsum dolor sit amet</li>
      <li><span style="color:var(--cyan)">✓</span> Lorem ipsum dolor sit amet</li>
    </ul>
    <div class="abs btn" style="left:23px;top:581px;width:43px;height:9px;line-height:9px">View Details</div>
    <div class="abs btn" style="left:73px;top:581px;width:43px;height:9px;line-height:9px">Contact Us</div>
    <div class="abs" style="left:202px;top:515px;width:106px;height:79px;background:linear-gradient(135deg,#3e5573,#1d2c45)" role="img" aria-label="Photo of a woman working at several computer screens"></div>
  </section>

  <section>
    <div class="abs" style="left:0;top:606px;width:180px;height:125px;background:linear-gradient(90deg,#2a3c78 0%,#8c3a6a 45%,#e9ecf2 100%)" role="img" aria-label="Illustration of a digital human head with network lines representing artificial intelligence"></div>
    <div class="abs" style="left:156px;top:636px;width:160px;height:30px;background:var(--navy)">
      <svg class="abs" style="left:8px;top:7px" width="16" height="16" viewBox="0 0 16 16"><circle cx="8" cy="8" r="7" fill="none" stroke="#fff" stroke-width=".8"/><circle cx="7.3" cy="7.3" r="2.6" fill="none" stroke="#fff" stroke-width=".8"/><path d="M9.2 9.2l2.3 2.3" stroke="#fff" stroke-width=".8"/></svg>
      <div class="abs" style="left:30px;top:5px;color:#fff;font-size:2.8px">ARE YOU LOOKING FOR AN ADVICE?</div>
      <p class="abs tiny" style="left:30px;top:10px;width:118px;color:#d2dbec;font-size:2.4px;line-height:3.8px">Lorem ipsum dolor sit amet, consectetur adipiscing elit. Proin eget ornare lacus, in ullamcorper dolor. Nulla rhoncus pellentesque hendrerit. Nullam mollis mauris sed gravida posuere.</p>
      <div class="abs" style="left:151px;top:12px;width:5px;height:5px;border-radius:50%;background:#fff"></div>
    </div>
    <div class="abs" style="left:156px;top:674px;width:160px;height:30px;background:var(--navy)">
      <svg class="abs" style="left:8px;top:7px" width="16" height="16" viewBox="0 0 16 16"><circle cx="8" cy="8" r="7" fill="none" stroke="#fff" stroke-width=".8"/><text x="8" y="11" text-anchor="middle" font-size="8" fill="#fff" font-family="Montserrat,sans-serif">$</text></svg>
      <div class="abs" style="left:30px;top:5px;color:#fff;font-size:2.8px">LOOKING FOR EARNING MONEY ?</div>
      <p class="abs tiny" style="left:30px;top:10px;width:118px;color:#d2dbec;font-size:2.4px;line-height:3.8px">Lorem ipsum dolor sit amet, consectetur adipiscing elit. Proin eget ornare lacus, in ullamcorper dolor. Nulla rhoncus pellentesque hendrerit. Nullam mollis mauris sed gravida posuere.</p>
      <div class="abs" style="left:151px;top:12px;width:5px;height:5px;border-radius:50%;background:#fff"></div>
    </div>
  </section>

  <section>
    <h2 class="abs" style="left:0;width:330px;top:744px;text-align:center;font-size:8px">Our Product</h2>
    <div class="abs" style="left:153px;top:756px;width:24px;height:.8px;background:var(--navy)"></div>
    <p class="abs tiny" style="left:38px;top:762px;width:254px;text-align:center">Lorem ipsum dolor sit amet, consectetur adipiscing elit. Proin eget ornare lacus, in ullamcorper dolor. Nulla rhoncus pellentesque hendrerit. Nullam mollis mauris sed gravida posuere.</p>
    <div class="abs pcard" style="left:22px;top:791px;width:85px;height:94px"><h3>LOREM IPSEM</h3><p>Lorem ipsum dolor sit amet, consectetur adipiscing elit. Proin eget ornare lacus, in ullamcorper dolor. Nulla rhoncus pellentesque hendrerit. Nullam mollis mauris sed gravida posuere. Praesent eu risus tortor.</p><div class="more">Read More</div></div>
    <div class="abs pcard" style="left:119px;top:791px;width:85px;height:94px"><h3>LOREM IPSEM</h3><p>Lorem ipsum dolor sit amet, consectetur adipiscing elit. Proin eget ornare lacus, in ullamcorper dolor. Nulla rhoncus pellentesque hendrerit. Nullam mollis mauris sed gravida posuere. Praesent eu risus tortor.</p><div class="more">Read More</div></div>
    <div class="abs pcard" style="left:215px;top:791px;width:85px;height:94px"><h3>LOREM IPSEM</h3><p>Lorem ipsum dolor sit amet, consectetur adipiscing elit. Proin eget ornare lacus, in ullamcorper dolor. Nulla rhoncus pellentesque hendrerit. Nullam mollis mauris sed gravida posuere. Praesent eu risus tortor.</p><div class="more">Read More</div></div>
  </section>

  <section class="abs" style="left:0;top:907px;width:330px;height:172px;background:linear-gradient(90deg,#1b3d78,#2c4f92)">
    <div class="abs" style="left:212px;top:0;width:118px;height:172px;background:linear-gradient(180deg,#3a5a98,#1c2f56)" role="img" aria-label="Photo of a businesswoman in a dark suit holding glasses"></div>
    <h2 class="abs" style="left:17px;top:13px;color:#fff;font-size:9px">Request A Call Back</h2>
    <div class="abs" style="left:17px;top:29px;width:28px;height:.8px;background:var(--cyan)"></div>
    <p class="abs tiny" style="left:16px;top:35px;width:196px;color:#d4dcec">Lorem ipsum dolor sit amet, consectetur adipiscing elit. Proin eget ornare lacus, in ullamcorper dolor. Nulla rhoncus pellentesque hendrerit. Nullam mollis mauris sed gravida posuere. Praesent eu risus tortor.</p>
    <div class="abs field" style="left:13px;top:64px;width:91px">First Name</div>
    <div class="abs field" style="left:112px;top:64px;width:90px">Last Name</div>
    <div class="abs field" style="left:13px;top:79px;width:91px">Email ID</div>
    <div class="abs field" style="left:112px;top:79px;width:90px">Phone no</div>
    <div class="abs field" style="left:13px;top:95px;width:189px;height:42px">Message</div>
    <div class="abs btn" style="left:13px;top:143px;width:189px;height:11px;line-height:11px">Submit Now</div>
  </section>

  <section>
    <h2 class="abs" style="left:23px;top:1091px;font-size:6.6px">Latest News</h2>
    <div class="abs" style="left:23px;top:1102px;width:20px;height:.8px;background:var(--cyan)"></div>
    <p class="abs tiny" style="left:23px;top:1108px;width:246px">Lorem ipsum dolor sit amet, consectetur adipiscing elit. Proin eget ornare lacus, in ullamcorper dolor. Nulla rhoncus pellentesque hendrerit. Nullam mollis mauris sed gravida posuere. Praesent eu risus tortor.</p>
    <svg class="abs" style="left:286px;top:1108px" width="28" height="12" viewBox="0 0 28 12"><rect x=".5" y=".5" width="11" height="11" fill="none" stroke="#1fb6e0"/><path d="M5 3.5l2.5 2.5L5 8.5" fill="none" stroke="#1fb6e0" stroke-width=".8"/><rect x="16.5" y=".5" width="11" height="11" fill="none" stroke="#1fb6e0"/></svg>

    <article class="abs news" style="left:22px;top:1137px;width:90px;height:151px">
      <div style="height:80px;background:linear-gradient(135deg,#9fb2c6,#4b5c70)" role="img" aria-label="Photo of hands typing on a laptop"></div>
      <h4>Lorem ipsum dolor sit amet, consectetur adipiscing elit</h4>
      <p>Lorem ipsum dolor sit amet, consectetur adipiscing elit. Proin eget ornare lacus, in ullamcorper dolor. Nulla rhoncus pellentesque hendrerit.</p>
      <div class="meta">▲ 56 Like &nbsp; ● 123 Comment</div>
    </article>
    <article class="abs news" style="left:123px;top:1137px;width:90px;height:151px">
      <div style="height:80px;background:linear-gradient(135deg,#6d5a48,#2a2724)" role="img" aria-label="Photo of a business team joining fists over a desk"></div>
      <h4>Lorem ipsum dolor sit amet, consectetur adipiscing elit</h4>
      <p>Lorem ipsum dolor sit amet, consectetur adipiscing elit. Proin eget ornare lacus, in ullamcorper dolor. Nulla rhoncus pellentesque hendrerit.</p>
      <div class="meta">▲ 23 Like &nbsp; ● 123 Comment</div>
    </article>
    <article class="abs news" style="left:224px;top:1137px;width:90px;height:151px">
      <div style="height:80px;background:linear-gradient(135deg,#d9b98a,#6b5a48)" role="img" aria-label="Photo of people working with a laptop and documents"></div>
      <h4>Lorem ipsum dolor sit amet, consectetur adipiscing elit</h4>
      <p>Lorem ipsum dolor sit amet, consectetur adipiscing elit. Proin eget ornare lacus, in ullamcorper dolor. Nulla rhoncus pellentesque hendrerit.</p>
      <div class="meta">▲ 136 Like &nbsp; ● 56 Comment</div>
    </article>
  </section>

  <footer class="abs foot">
    <div class="abs brand" style="left:20px;top:17px;color:#fff;font-size:9px;font-weight:400">Tarvolin</div>
    <p class="abs tiny" style="left:20px;top:38px;width:84px;color:#cdd6e8">Lorem ipsum dolor sit amet, consectetur adipiscing elit. Proin eget ornare lacus, in ullamcorper dolor. Nulla rhoncus pellentesque hendrerit. Nullam mollis mauris sed gravida posuere. Praesent eu risus tortor.</p>
    <svg class="abs" style="left:21px;top:72px" width="34" height="6" viewBox="0 0 34 6"><circle cx="3" cy="3" r="2.2" fill="#fff"/><circle cx="11" cy="3" r="2.2" fill="#fff"/><circle cx="19" cy="3" r="2.2" fill="#fff"/><circle cx="27" cy="3" r="2.2" fill="#fff"/></svg>
    <h5 class="abs" style="left:133px;top:20px">Links</h5>
    <ul class="abs" style="left:133px;top:33px"><li>✓ Home</li><li>✓ About Us</li><li>✓ Product</li><li>✓ Service</li><li>✓ News</li><li>✓ Contact Us</li></ul>
    <h5 class="abs" style="left:199px;top:20px">Location</h5>
    <div class="abs" style="left:199px;top:32px;font-size:5px;line-height:9px;color:#cdd6e8">Dummy city,<br>Dummy country land</div>
    <div class="abs" style="left:199px;top:56px;font-size:3.6px;line-height:7.5px">☏ 000.0000.000<br>⎙ 000.0000.000<br>✉ info@tarvolin-example.com</div>
    <div class="abs" style="left:20px;top:93px;width:290px;height:.5px;background:#4a6498"></div>
    <div class="abs" style="left:0;width:330px;top:98px;text-align:center;font-size:3.6px;color:#cdd6e8">2018 Tarvolin. All Copyright Reserved.</div>
  </footer>

</main>
</div>
</body>
</html>
```